Website for Nonprofit for kids whose parents have been wounded

We need a web design for a nonprofit that serves children who have been severely burned as well as those whose parents have been wounded during military service. We will be based out of hospitals and will need a format that will encourage trust, safety, and respect. We are stick with a lot of red white and blue. We will also be looking to have a space for donations.

Target Market(s)

Kids and parents of military veterans

Industry/Entity Type

Non Profit

Number of Pages Required

5+ page

Font styles to use
Serif
Decorative

Colors
ec1f27
ffffff
0255a3

Requirements
Must have
• Be both appealing to children and adults. Create a reputable face for our organization. We need an area for donations.
Nice to have
• Something unique

```html
<!DOCTYPE html>
<html lang="en">
<head>
<meta charset="utf-8">
<title>Kids Support Foundation</title>
<link href="https://fonts.googleapis.com/css2?family=Open+Sans:wght@400;600;700&display=swap" rel="stylesheet">
<style>
:root{
  --red:#ec1f27;
  --blue:#0255a3;
  --navy:#1b3f73;
  --white:#ffffff;
  --dark:#1e1e1e;
  --darker:#141414;
  --grey-text:#9a9a9a;
  --body-text:#666666;
  --footer-bg:#e9e9e9;
}
*{margin:0;padding:0;box-sizing:border-box}
html,body{width:805px;height:1200px;overflow:hidden}
body{font-family:"Open Sans",Arial,sans-serif;background:var(--white);color:var(--body-text);position:relative}
.site-header{position:absolute;top:0;left:0;width:805px;height:96px}
.brand{position:absolute;left:30px;top:38px;font-weight:600;font-size:18px;color:var(--blue);line-height:22px}
.main-nav{position:absolute;right:22px;top:38px;display:flex;gap:6px}
.main-nav a{display:block;font-size:9px;font-weight:600;color:#555;text-decoration:none;padding:8px 12px;text-transform:uppercase}
.main-nav a.active{background:var(--red);color:var(--white)}
.hero{position:absolute;left:27px;top:100px;width:751px;height:300px;background:linear-gradient(120deg,#6f9aa6 0%,#a9b9a3 45%,#8c8562 75%,#4d5a3c 100%)}
.hero-caption{position:absolute;left:165px;top:205px;width:300px;background:rgba(30,40,50,.55);color:var(--white);font-size:13px;line-height:1.45;padding:8px 12px}
.hero-arrow{position:absolute;top:136px;width:22px;height:22px;fill:none;stroke:var(--white);stroke-width:3}
.hero-arrow.prev{left:10px}.hero-arrow.next{right:10px}
.hero-dots{position:absolute;bottom:12px;left:50%;transform:translateX(-50%);display:flex;gap:6px}
.hero-dots span{width:8px;height:8px;border-radius:50%;background:rgba(255,255,255,.6)}
.hero-dots span.on{background:var(--white)}
.intro{position:absolute;top:412px;left:0;width:805px;height:238px;background:var(--dark);color:var(--grey-text)}
.intro h2{color:var(--white);font-size:22px;font-weight:700;margin-bottom:12px;text-transform:uppercase}
.welcome{position:absolute;left:27px;top:24px;width:470px}
.welcome p{font-size:9.5px;line-height:1.75}
.btn{display:inline-block;background:var(--red);color:var(--white);font-size:9px;font-weight:700;text-transform:uppercase;padding:9px 16px;margin-top:16px;text-decoration:none}
.news{position:absolute;left:540px;top:24px;width:238px}
.news-item{margin-bottom:10px;font-size:9px;line-height:1.5}
.news-item time{display:block;color:var(--white);font-weight:700;font-size:9px}
.donation{position:absolute;top:650px;left:0;width:805px;height:172px;background:var(--blue);color:#dbe6f3;text-align:center;padding:24px 60px 0}
.donation h2{color:var(--white);font-size:22px;font-weight:700;text-transform:uppercase;margin-bottom:8px}
.donation p{font-size:9.5px;line-height:1.7}
.apply{position:absolute;top:848px;left:0;width:805px;height:220px}
.apply h2{position:absolute;left:27px;top:14px;color:var(--blue);font-size:19px;font-weight:700;text-transform:uppercase}
.apply-rule{position:absolute;left:27px;top:44px;width:470px;height:1px;background:#ddd}
.apply p{position:absolute;left:27px;width:470px;font-size:9.5px;line-height:1.75}
.apply p.first{top:56px}.apply p.second{top:138px}
.apply-video{position:absolute;left:530px;top:14px;width:248px;height:162px;background:linear-gradient(135deg,#9fb4c2,#c9b8a2 55%,#6d7a63)}
.video-bar{position:absolute;left:0;bottom:0;width:100%;height:20px;background:rgba(0,0,0,.7)}
.video-bar svg{position:absolute;left:8px;top:5px}
.video-progress{position:absolute;left:28px;right:10px;top:9px;height:2px;background:#888}
.site-footer{position:absolute;top:1072px;left:0;width:805px;height:104px;background:var(--footer-bg);display:flex;padding:16px 27px 0;gap:22px}
.site-footer h3{font-size:10px;font-weight:700;color:#333;text-transform:uppercase;margin-bottom:7px}
.site-footer li{list-style:none;font-size:8.5px;line-height:1.7;color:#666}
.col-news{width:200px;font-size:8.5px}
.signup{display:flex;margin-top:6px}
.signup span{flex:1;height:22px;background:var(--white);border:1px solid #ccc}
.signup b{background:var(--red);color:var(--white);font-size:9px;padding:5px 10px}
.col{width:100px}
.follow li{display:flex;align-items:center;gap:5px}
.follow li i{width:9px;height:9px;background:var(--blue);display:block}
.copyright{position:absolute;top:1176px;left:0;width:805px;height:24px;background:var(--darker);color:#888;font-size:8.5px;text-align:center;line-height:24px}
</style>
</head>
<body>
<header class="site-header">
  <div class="brand">Kids Support Foundation</div>
  <nav class="main-nav">
    <a class="active" href="#">Home</a><a href="#">Our Games</a><a href="#">Our Mission</a><a href="#">How to Apply</a><a href="#">Contact Us</a>
  </nav>
</header>

<section class="hero" role="img" aria-label="Photo of a soldier in uniform hugging a young child">
  <svg class="hero-arrow prev" viewBox="0 0 22 22"><path d="M14 3 6 11l8 8"/></svg>
  <svg class="hero-arrow next" viewBox="0 0 22 22"><path d="M8 3l8 8-8 8"/></svg>
  <p class="hero-caption">We serve children who have been severely burned as well as those whose parents have been wounded during military service.</p>
  <div class="hero-dots"><span class="on"></span><span></span><span></span></div>
</section>

<section class="intro">
  <div class="welcome">
    <h2>Welcome to KSF</h2>
    <p>We work inside hospitals to bring comfort, play and steady support to children facing burns or a parent's injury. Our volunteers offer games, mentoring and safe spaces where kids can simply be kids again. Families receive guidance, respite and a caring community that stands beside them through recovery. Every program is built on trust, safety and respect, and every visit is shaped around the needs of the child and the family we serve together.</p>
    <a class="btn" href="#">Read More</a>
  </div>
  <div class="news">
    <h2>Latest News</h2>
    <div class="news-item"><time>AUG 13 2015</time>New game room opens at our partner hospital this week.</div>
    <div class="news-item"><time>AUG 13 2015</time>Summer camp dates announced for military families.</div>
    <div class="news-item"><time>AUG 13 2015</time>Volunteers gather to pack care kits for young patients.</div>
  </div>
</section>

<section class="donation">
  <h2>Donation Meter</h2>
  <p>Your gift helps us reach children in hospitals across the country. Every donation funds games, care kits and family support programs. See how close we are to this year's goal and help us bring comfort to more kids and parents who need it most.</p>
  <a class="btn" href="#">Click Here</a>
</section>

<section class="apply">
  <h2>How to Apply?</h2>
  <div class="apply-rule"></div>
  <p class="first">Families can apply through our hospital liaisons or by completing a short form online. We ask a few simple questions about your child, your care team and the support you are hoping for, so we can match you with the right program quickly and kindly.</p>
  <p class="second">Once we receive your form, a member of our team will reach out within a few days to talk through next steps and answer any questions you have.</p>
  <div class="apply-video" role="img" aria-label="Video still of a parent and child together">
    <div class="video-bar"><svg width="10" height="10" viewBox="0 0 10 10"><path d="M1 0l8 5-8 5z" fill="#fff"/></svg><div class="video-progress"></div></div>
  </div>
</section>

<footer class="site-footer">
  <div class="col-news"><h3>Newsletter</h3>Enter your email to stay updated.<div class="signup"><span></span><b>GO</b></div></div>
  <div class="col follow"><h3>Follow Us</h3><ul><li><i></i>Community</li><li><i></i>Updates</li><li><i></i>Videos</li></ul></div>
  <div class="col"><h3>About Us</h3><ul><li>Who We Help?</li><li>Our Mission</li><li>Our Team</li><li>Partners</li></ul></div>
  <div class="col"><h3>Blog</h3><ul><li>Jun 2015</li><li>Jul 2015</li><li>Aug 2015</li></ul></div>
  <div class="col"><h3>Quick Links</h3><ul><li>Privacy Policy</li><li>Terms &amp; Conditions</li><li>Site Map</li></ul></div>
</footer>
<div class="copyright">Copyright © 2015 Kids Support Foundation. All Rights Reserved.</div>
</body>
</html>
```